Growing Wellness Company Needs an Amazing Cover for a series of Booklets

We are publishing our own series of booklets on health & wellness topics, called Vital Spark Primers and need an inspiring, modern design for the cover. We are beginning with the Title Diabetes: Type 2, but we will use this design for other titles later one.

SIZE:
This will be the front and back of a 8.5 x 5.5 booklet, plus 2 sample interior pages.

COLOR:
We are an industry leaders and prefer touse vibrant colors and designs to inspire our clients to change to a healthier lifestyle.

REQUIREMENTS:
I am attaching our Vital Spark logo, which needs to be on each cover, but does not need to be the focal point. You may you the words vital spark or just the b logo. The topic/title needs to be no lower than 1/2" from the top of the cover.

I'm attaching some samples of items I like, but please be creative!
If you would like to see some of our other in-house samples of publications send me a message and I'll show you. I will give detailed feedback so dive in and get creative!
Updates

FRONT COVER: 
1. Can you please make sure the title is in the top 1.5" of the page, i can't tell from this view. 
Type 2 Diabetes (1st line, bigger) 
A Simple Guide to Understanding & Controlling Your Blood Sugar (Second Row, much smaller) this can also be below the 1.5" line if it needs to be. 
3.We would like to see three shapes maybe toward the bottom with these words in them, one word per shape. inspire, equip, succeed 

IMAGE 
1. We would like you to leave a placeholder for an image, but would like to see different shapes, such as a rounded square or rectangle or a rectangle with two square corners and two rounded corners. 
2. Please play with some different border options as well,

BACKSIDE 
1. please put our information on the back side on the bottom, small. the information i will put in a file on the brief, the 2nd page has our address, phone, etc. 
2. Add our MC logo (attached as an image in the design brief)

Thanks! looking forward to what else you have. 

Reason: I want to give more time to get more/better designs in, i know this is a little more involved project.

Reason: Still not happy with designs, would like to see more.

Hello - thank you for submitting designs, the designs are getting a little too busy....here is a website I love the simplicity of...thanks!  http://www.brindlevalecare.example   

Reason: We are getting closer to narrowing it down, I want to give the designers a few more days to tweak their designs, then i will ask the final 2 or 3 to submit a couple version of the inside pages. I will supply text for those so you know what you're working with. Thanks!

Target Market(s)

Our clients are adults, about 50/50 men & women in the age range from 20-70 with most being in their early 50's. from high school education up to professional degrees

Industry/Entity Type

Industry

Font styles to use
Serif
Sans Serif
Script

Colors
a64599
e34197
00a98f
9bcb3c
ffc214
f78f20
f37122
0492cd
6a439a

Requirements
Must have
• Eye catching, inspiring design that entices people to read our booklet:

I need a front and back cover and 2 interior page samples , we will be using more of an info graphic style inside possible with a few actual photographs

FRONT COVER REQUIREMENTS:
Title (must be no lower than 1.5" below the top)
Vital Spark Logo (attached in pink and green)
Meadowcrest Wellness' Logo

BACK COVER REQUIREMENTS:
a place for summary text
meadowcrest wellness contact information
a place for an item # (can be small, no barcode)
Nice to have
• the colors i chose are samples, does not need to include every color, each title we write will have a different color story

I can appreciate a white cover with some amazing art of pops of color, but i would also love a really rich color with subtle tone on tone things (see the navy blue cover picture)
Should not have
• boring colors, lots of pictures, typical booklet design

```html
<!DOCTYPE html>
<html lang="en">
<head>
<meta charset="utf-8">
<title>Vital Spark Primers – Type 2 Diabetes Cover</title>
<link rel="stylesheet" href="https://fonts.googleapis.com/css2?family=Oswald:wght@300;400&family=Open+Sans:wght@400;600&display=swap">
<style>
  :root {
    --lime: #d6ef2e;
    --lime-soft: #e4f56a;
    --leaf: #8fd61c;
    --leaf-deep: #5cbf14;
    --orchid: #e79be6;
    --orchid-soft: #f3c9ef;
    --amber: #f2c23a;
    --ink: #1e1e1e;
    --grey-text: #8a8a8a;
    --white: #ffffff;
    --blob-lime: #c9ec1a;
    --blob-pink: #e96f9c;
    --blob-teal: #35d48a;
    --frame: #2a2a2a;
  }
  * { box-sizing: border-box; margin: 0; padding: 0; }
  html, body { width: 1200px; height: 923px; overflow: hidden; background: var(--white); }
  body { position: relative; font-family: "Open Sans", Arial, sans-serif; }

  .panel-label {
    position: absolute; top: 8px;
    font-family: "Open Sans", Arial, sans-serif; font-size: 27px; color: #000; font-weight: 400;
  }
  .panel-label--back { left: 48px; }
  .panel-label--front { left: 630px; }

  .cover { position: absolute; top: 47px; height: 853px; overflow: hidden; }
  .cover--back { left: 50px; width: 551px; border: 1px solid var(--frame); }
  .cover--front { left: 604px; width: 551px; }

  .artwork { position: absolute; inset: 0; }
  .artwork--back {
    background:
      radial-gradient(ellipse 60% 30% at 40% 65%, rgba(150,215,20,.55), transparent 70%),
      radial-gradient(ellipse 50% 25% at 30% 10%, rgba(160,220,30,.6), transparent 70%),
      linear-gradient(160deg, var(--lime-soft) 0%, var(--lime) 45%, #cdea22 70%, var(--lime-soft) 100%);
  }
  .artwork--front {
    left: 88px;
    background:
      radial-gradient(ellipse 40% 20% at 85% 10%, rgba(255,255,220,.9), transparent 70%),
      radial-gradient(ellipse 55% 30% at 45% 40%, var(--orchid-soft), transparent 75%),
      radial-gradient(ellipse 45% 25% at 70% 85%, rgba(120,210,20,.8), transparent 70%),
      linear-gradient(170deg, #b6e02a 0%, var(--orchid) 25%, #f0d4f0 48%, #c8e86a 68%, var(--leaf) 82%, var(--amber) 100%);
  }
  .spine-strip {
    position: absolute; left: 0; top: 0; width: 88px; bottom: 60px;
    background: linear-gradient(180deg, #e2f24a 0%, #d4ec30 50%, #dcef3a 100%);
  }

  .drops-band {
    position: absolute; left: 0; right: 0; bottom: 0; height: 60px;
    background: linear-gradient(180deg, #a6e61c 0%, var(--leaf-deep) 55%, #8ed81a 100%);
  }
  .cover--front .drops-band { border-top: 3px solid var(--white); height: 62px; }

  .brand-mark {
    position: absolute; font-family: "Open Sans", Arial, sans-serif;
    font-weight: 600; font-size: 17px; color: var(--leaf); letter-spacing: .5px;
  }
  .cover--back .brand-mark { left: 40px; top: 58px; }
  .cover--front .brand-mark { right: 28px; top: 62px; }

  .partner-badge {
    position: absolute; width: 96px; height: 96px; border-radius: 14px;
    background: var(--white); display: flex; align-items: center; justify-content: center;
    font-family: "Open Sans", Arial, sans-serif; font-weight: 600; font-size: 34px; color: #c9dc1e;
  }
  .cover--back .partner-badge { left: 28px; top: 705px; }
  .cover--front .partner-badge { right: 27px; top: 702px; }

  /* vertical text reading bottom to top */
  .upright-rotated {
    position: absolute; writing-mode: vertical-rl; transform: rotate(180deg);
    white-space: nowrap; line-height: 1;
  }

  .contact-line {
    left: 519px; bottom: 83px;
    font-family: "Open Sans", Arial, sans-serif; font-size: 12px; color: var(--ink);
    letter-spacing: -.1px;
  }

  .title {
    left: 42px; top: 61px;
    font-family: "Oswald", "Arial Narrow", sans-serif; font-weight: 300;
    font-size: 32px; color: var(--white); letter-spacing: -.3px;
  }
  .subtitle {
    left: 94px; top: 61px;
    font-family: "Open Sans", Arial, sans-serif; font-size: 13px; color: var(--grey-text);
  }

  .values { position: absolute; left: 100px; top: 665px; width: 150px; height: 150px; }
  .values text {
    font-family: "Open Sans", Arial, sans-serif; font-size: 13.5px; fill: var(--white);
  }
</style>
</head>
<body>
  <div class="panel-label panel-label--back">Back Cover</div>
  <div class="panel-label panel-label--front">Front Cover</div>

  <section class="cover cover--back" aria-label="Back cover">
    <div class="artwork artwork--back" role="img" aria-label="Soft-focus lime green botanical background with translucent leaf shapes"></div>
    <div class="brand-mark">Vital Spark</div>
    <p class="upright-rotated contact-line">Meadowcrest Wellness LLC | 218 Elm Street | P.O. Box 732 | Fairhaven, NE 68999 | meadowcrest.example | 555.014.2290</p>
    <div class="partner-badge">MC</div>
    <div class="drops-band" role="img" aria-label="Close-up of water droplets on a green leaf"></div>
  </section>

  <section class="cover cover--front" aria-label="Front cover">
    <div class="artwork artwork--front" role="img" aria-label="Soft-focus pink and green botanical background with leaf blades and sparkles"></div>
    <div class="spine-strip"></div>
    <h1 class="upright-rotated title">Type 2 Diabetes</h1>
    <p class="upright-rotated subtitle">Simple guide to understanding and controlling your blood sugar</p>
    <div class="brand-mark">Vital Spark</div>
    <svg class="values" viewBox="0 0 150 150" aria-label="Inspire, Equip, Succeed">
      <ellipse cx="82" cy="42" rx="38" ry="34" fill="var(--blob-lime)" opacity=".92"/>
      <ellipse cx="37" cy="107" rx="36" ry="33" fill="var(--blob-pink)" opacity=".85"/>
      <ellipse cx="100" cy="110" rx="40" ry="33" fill="var(--blob-teal)" opacity=".85"/>
      <text x="72" y="47" text-anchor="middle">Inspire</text>
      <text x="28" y="115" text-anchor="middle">Equip</text>
      <text x="97" y="111" text-anchor="middle">Succeed</text>
    </svg>
    <div class="partner-badge">MC</div>
    <div class="drops-band" role="img" aria-label="Close-up of water droplets on a green leaf"></div>
  </section>
</body>
</html>
```